Dr. Lumora needs a design for its website!

*Only need the design, coding is not required.
*Need desktop version ($500) and mobile/tablet version ($200)
*The attached files are not the exact layout we want, they are just for you to know what information should be included in those pages.
*The function of our website is like www.qavlo.hk
*For the background picture, prefer a lively picture and chinese people in it, NOT necessarily need a doctor or sick person in the picture

***Don't just copy the layout from the attachments or from the reference website, we are looking for creative ideas, non-ordinary designs!!!****

We are developing a website for the public to search a doctor by different criteria. At the initial stage, we need 4 pages to start with and other pages at later stage. I have attached the general idea of these pages but not necessarily to be exactly the same, I am looking for some new ideas.

This website needs a professional, modern, simple and user friendly design. The main color to be used in the website will be same as the color (R:0 G:139 B:205) used in our logo (see attached). We don't have any particular thoughts for the other color and the font to be used in the website. Can try to use circle outline for the icon in the navigation bar.

1. Home: will include 4 sections (see attached)

2. Doctor's details (see attached)

3. Health information: will include a short descriptions of this Health Info page and 5 sections (see attached)

4. News (see attached)

Reason: Not too many suitable designs to choose from and need more time to go through the designs

All

Medical

4 page

• must not be same as or looks too much like www.qavlo.hk
• prefer not to use black and red color

```html
<!DOCTYPE html>
<html lang="en">
<head>
<meta charset="utf-8">
<title>Dr. Lumora – Home</title>
<link href="https://fonts.googleapis.com/css2?family=Dosis:wght@500;600;700&family=Raleway:wght@400;500;600;700&display=swap" rel="stylesheet">
<style>
:root{
  --brand:#0888cd;
  --brand-dark:#0a6aa3;
  --ink:#2b2b2b;
  --muted:#555;
  --panel:rgba(255,255,255,.82);
  --field:#ffffff;
  --line:#d5d5d5;
  --footer:#333336;
}
*{box-sizing:border-box;margin:0;padding:0}
html,body{width:1200px;height:926px;overflow:hidden;background:#fff}
body{position:relative;font-family:"Raleway",sans-serif;color:var(--ink)}
.abs{position:absolute}

/* header */
.site-header{position:absolute;left:0;top:0;width:1200px;height:131px;background:#fff}
.brand{position:absolute;left:99px;top:30px;display:flex;align-items:center;gap:12px}
.brand-dot{width:56px;height:56px;border-radius:50%;background:var(--brand)}
.brand-name{font-family:"Raleway",sans-serif;font-weight:500;font-size:39px;color:var(--brand);letter-spacing:-.5px}
.top-search{position:absolute;left:805px;top:8px;width:154px;height:41px;border:1px solid #333;display:flex;align-items:center;justify-content:space-between;padding:0 12px 0 21px;font-family:"Dosis",sans-serif;font-weight:600;font-size:18px;color:#333;letter-spacing:.5px}
.lang{position:absolute;left:972px;top:8px;width:128px;height:41px;border:1px solid var(--brand);display:flex;align-items:center;gap:10px;padding-left:8px;font-family:"Raleway",sans-serif;font-weight:700;font-size:13px;color:#222}
.lang-swatch{width:30px;height:22px;background:#c8d4e8}
.main-nav{position:absolute;top:80px;left:0;width:1200px;font-family:"Dosis",sans-serif;font-weight:700;font-size:17px;color:#222;letter-spacing:.3px}
.main-nav span{position:absolute;white-space:nowrap}
.main-nav .active{color:var(--brand)}

/* hero */
.hero-bg{position:absolute;left:0;top:131px;width:1200px;height:735px;
  background:
   radial-gradient(ellipse 380px 420px at 1040px 300px,#e9b48f 0%,rgba(233,180,143,0) 70%),
   radial-gradient(ellipse 420px 300px at 760px 560px,#d9a1a6 0%,rgba(217,161,166,0) 70%),
   radial-gradient(ellipse 500px 400px at 180px 300px,#b9c28a 0%,rgba(185,194,138,0) 75%),
   linear-gradient(180deg,#9fae72 0%,#c9cfa0 45%,#b6c48c 75%,#8fa46a 100%)}

.panel{position:absolute;background:var(--panel)}
.panel-title{height:55px;background:var(--brand);color:#fff;font-family:"Dosis",sans-serif;font-weight:700;font-size:24px;letter-spacing:.3px;display:flex;align-items:center;padding-left:24px}

/* search doctor */
.search-doctor{left:99px;top:159px;width:462px;height:458px}
.form-label{position:absolute;left:25px;font-size:16px;font-weight:500;color:#222}
.field{position:absolute;left:150px;width:285px;height:39px;background:var(--field);border:1px solid var(--line);border-radius:2px}
.field.select::after{content:"";position:absolute;right:16px;top:16px;border-left:7px solid transparent;border-right:7px solid transparent;border-top:8px solid #444}
.check-box{position:absolute;width:43px;height:39px;background:#fff;border:1px solid var(--line);border-radius:2px;display:flex;align-items:center;justify-content:center}
.check-label{position:absolute;font-size:18px;font-weight:500;color:#222}
.btn{position:absolute;height:42px;color:#fff;font-family:"Dosis",sans-serif;font-weight:700;font-size:19px;display:flex;align-items:center;justify-content:space-between;padding:0 14px 0 15px;letter-spacing:.3px}
.btn-light{background:var(--brand)}
.btn-dark{background:var(--brand-dark);padding-left:18px}

/* login */
.member-login{left:575px;top:159px;width:526px;height:242px}
.login-row{position:absolute;left:25px;width:467px;height:39px;display:flex;border:1px solid var(--line);background:#fff;border-radius:2px}
.login-icon{width:63px;background:#f2f2f2;border-right:1px solid var(--line);display:flex;align-items:center;justify-content:center}
.login-text{padding-left:18px;display:flex;align-items:center;font-size:16px;font-weight:500;color:#222}
.forgot{position:absolute;left:327px;top:185px;display:flex;align-items:center;gap:12px;font-size:16px;font-weight:500;color:#222}
.forgot .check-box{position:static;width:27px;height:27px}

/* membership */
.membership{left:575px;top:415px;width:526px;height:202px}
.perk{position:absolute;display:flex;align-items:center;gap:19px;font-size:15.5px;font-weight:500;color:#222;white-space:nowrap}
.tick{width:17px;height:17px;background:var(--brand);display:flex;align-items:center;justify-content:center}
.learn-more{position:absolute;left:304px;top:149px;font-family:"Dosis",sans-serif;font-weight:700;font-size:18px;color:#222;text-decoration:underline}

/* results table */
.results{position:absolute;left:99px;top:631px;width:1002px;border-collapse:collapse;background:rgba(255,255,255,.78);table-layout:fixed}
.results th{height:70px;background:var(--brand);color:#fff;font-family:"Dosis",sans-serif;font-weight:700;font-size:19px;letter-spacing:.3px;border-right:1px solid rgba(255,255,255,.35)}
.results td{height:44px;text-align:center;font-size:13.5px;font-weight:500;color:#222;border-right:1px dashed #ddd;border-bottom:1px dashed #ddd}
.results th:last-child,.results td:last-child{border-right:none}
.results tr.empty td{height:46px;border-bottom:none}

/* footer */
.site-footer{position:absolute;left:0;top:866px;width:1200px;height:60px;background:var(--footer)}
.copyright{position:absolute;left:100px;top:20px;color:#fff;font-weight:700;font-size:14.5px}
.social{position:absolute;left:937px;top:9px;display:flex;gap:8px}
.social span{width:36px;height:36px;border-radius:50%}
</style>
</head>
<body>

<header class="site-header">
  <div class="brand"><span class="brand-dot"></span><span class="brand-name">Dr. Lumora</span></div>
  <div class="top-search">Search
    <svg width="20" height="20" viewBox="0 0 20 20"><circle cx="8" cy="8" r="6" fill="none" stroke="#333" stroke-width="2"/><path d="M12.5 12.5l5 5" stroke="#333" stroke-width="2.2" stroke-linecap="round"/></svg>
  </div>
  <div class="lang"><span class="lang-swatch"></span>ENGLISH
    <svg width="8" height="5" viewBox="0 0 8 5"><path d="M0 0h8L4 5z" fill="#222"/></svg>
  </div>
  <nav class="main-nav">
    <span class="active" style="left:528px">Home</span>
    <span style="left:615px">TBC</span>
    <span style="left:686px">Health Info</span>
    <span style="left:814px">News</span>
    <span style="left:897px">About Us</span>
    <span style="left:1010px">Contact Us</span>
  </nav>
</header>

<div class="hero-bg" role="img" aria-label="Background photo of a cheerful family outdoors in a sunny park"></div>

<section class="panel search-doctor">
  <div class="panel-title">Search Doctor</div>
  <span class="form-label" style="top:90px">Doctor Name</span>
  <div class="field" style="top:78px"></div>

  <span class="form-label" style="top:142px">Gender</span>
  <div class="check-box" style="left:150px;top:129px">
    <svg width="22" height="18" viewBox="0 0 22 18"><path d="M2 9l6 6L20 2" fill="none" stroke="#111" stroke-width="2.2"/></svg>
  </div>
  <span class="check-label" style="left:204px;top:139px">Male</span>
  <div class="check-box" style="left:280px;top:129px"></div>
  <span class="check-label" style="left:334px;top:139px">Female</span>

  <span class="form-label" style="top:190px">Specialism</span>
  <div class="field select" style="top:180px"></div>

  <span class="form-label" style="top:243px">Symptoms</span>
  <div class="field select" style="top:231px"></div>

  <span class="form-label" style="top:295px">District</span>
  <div class="field select" style="top:282px"></div>

  <span class="form-label" style="top:344px">Phone Number</span>
  <div class="field" style="top:333px"></div>

  <div class="btn btn-light" style="left:150px;top:384px;width:135px">Reset
    <svg width="18" height="18" viewBox="0 0 18 18"><path d="M15 9a6 6 0 1 1-2-4.5" fill="none" stroke="#fff" stroke-width="2.4"/><path d="M11 2h5v5z" fill="#fff"/></svg>
  </div>
  <div class="btn btn-dark" style="left:296px;top:384px;width:136px">Search
    <svg width="18" height="18" viewBox="0 0 20 20"><circle cx="8" cy="8" r="6" fill="none" stroke="#fff" stroke-width="2"/><path d="M12.5 12.5l5 5" stroke="#fff" stroke-width="2.2" stroke-linecap="round"/></svg>
  </div>
</section>

<section class="panel member-login">
  <div class="panel-title">Member Login</div>
  <div class="login-row" style="top:77px">
    <div class="login-icon"><svg width="18" height="22" viewBox="0 0 18 22"><path d="M4 10V6a5 5 0 0 1 10 0v4" fill="none" stroke="#555" stroke-width="2.4"/><rect x="1" y="10" width="16" height="12" rx="2" fill="#555"/></svg></div>
    <div class="login-text">Username</div>
  </div>
  <div class="login-row" style="top:127px">
    <div class="login-icon"><svg width="26" height="22" viewBox="0 0 26 22"><circle cx="9" cy="6" r="5" fill="#555"/><path d="M0 22c0-6 4-9 9-9s9 3 9 9z" fill="#555"/><circle cx="20" cy="16" r="4.5" fill="#fff" stroke="#555" stroke-width="1.6"/></svg></div>
    <div class="login-text">PassWord</div>
  </div>
  <div class="btn btn-light" style="left:25px;top:179px;width:110px;height:37px">Log In
    <svg width="17" height="20" viewBox="0 0 18 22"><path d="M4 10V6a5 5 0 0 1 10 0" fill="none" stroke="#fff" stroke-width="2.4"/><rect x="1" y="10" width="16" height="12" rx="2" fill="#fff"/></svg>
  </div>
  <div class="forgot">
    <span class="check-box"><svg width="15" height="12" viewBox="0 0 22 18"><path d="M2 9l6 6L20 2" fill="none" stroke="#111" stroke-width="2.6"/></svg></span>
    Forgot Password
  </div>
</section>

<section class="panel membership">
  <div class="panel-title">Become A Dr. Lumora Member</div>
  <div class="perk" style="left:26px;top:84px"><span class="tick"><svg width="11" height="9" viewBox="0 0 22 18"><path d="M2 9l6 6L20 2" fill="none" stroke="#fff" stroke-width="3"/></svg></span>First-hand Health News</div>
  <div class="perk" style="left:26px;top:118px"><span class="tick"><svg width="11" height="9" viewBox="0 0 22 18"><path d="M2 9l6 6L20 2" fill="none" stroke="#fff" stroke-width="3"/></svg></span>Free Health Seminars / talks</div>
  <div class="perk" style="left:26px;top:152px"><span class="tick"><svg width="11" height="9" viewBox="0 0 22 18"><path d="M2 9l6 6L20 2" fill="none" stroke="#fff" stroke-width="3"/></svg></span>Priority Doctor Appointments</div>
  <div class="perk" style="left:306px;top:84px"><span class="tick"><svg width="11" height="9" viewBox="0 0 22 18"><path d="M2 9l6 6L20 2" fill="none" stroke="#fff" stroke-width="3"/></svg></span>Exclusive Promotions</div>
  <div class="perk" style="left:306px;top:118px"><span class="tick"><svg width="11" height="9" viewBox="0 0 22 18"><path d="M2 9l6 6L20 2" fill="none" stroke="#fff" stroke-width="3"/></svg></span>Instant Health Advices</div>
  <a class="learn-more">Learn More</a>
</section>

<table class="results">
  <colgroup>
    <col style="width:110px"><col style="width:126px"><col style="width:154px"><col style="width:112px">
    <col style="width:112px"><col style="width:129px"><col style="width:116px"><col style="width:143px">
  </colgroup>
  <thead>
    <tr><th>Name</th><th>Gender</th><th>Specialism</th><th>Lorem</th><th>Lorem</th><th>Address</th><th>District</th><th>Phone No</th></tr>
  </thead>
  <tbody>
    <tr><td>Dr. Ravel</td><td>Male</td><td>Lorem Ipsum</td><td>Private</td><td>Lorem Ipsum</td><td>Lorem Ipsum-123</td><td>Lorem</td><td>0123-456-789</td></tr>
    <tr><td>Dr. Oskin</td><td>Female</td><td>Lorem Ipsum</td><td>Private</td><td>Lorem Ipsum</td><td>Lorem Ipsum-123</td><td>Lorem</td><td>0123-456-789</td></tr>
    <tr class="empty"><td></td><td></td><td></td><td></td><td></td><td></td><td></td><td></td></tr>
  </tbody>
</table>

<footer class="site-footer">
  <p class="copyright">Copyright © Dr. Lumora. All Right Reserved</p>
  <div class="social" aria-label="Social links">
    <span style="background:#3b5a9a"></span>
    <span style="background:#1da1e2"></span>
    <span style="background:#2b8fc4"></span>
    <span style="background:#d4473a"></span>
  </div>
</footer>

</body>
</html>
```